I want to sell a virtual ticket that captures customers details.

Using this information, i manually write the customers details on a piece of paper and enter them into a draw/raffle to potentially win a watch. I dont need random generators/software to pick winners, as law mandates this process to be physically done. All i need is a nice website that allows customers to purchase and enter. I have posted a few links below in the description. If you refer to orvanteltrading.com, you will see what i am after. I have my own site www.thekestrelmarque.com.au but i dont like how it looks and i want something better. I hope this will give you an idea on what i am after.

Target Market(s)

adults aged approximately 24-56

Industry/Entity Type

luxury watches / contestant giveaways

Number of Pages Required

4 page

Font styles to use
Serif
Other font styles liked:
• something classy - i am not sure

Colors

Designer to choose only greyscale colors for use in the design.

Requirements
Must have
• Stripe payment software

```html
<!DOCTYPE html>
<html lang="en">
<head>
<meta charset="utf-8">
<title>The Kestrel Marque — Watch Draws</title>
<link rel="stylesheet" href="https://fonts.googleapis.com/css2?family=Playfair+Display:wght@400&family=Montserrat:wght@400;500;600&display=swap">
<style>
:root{
  --ink:#1f1f1f;
  --navy:#23232f;
  --text:#555;
  --muted:#888;
  --line:#bdbdbd;
  --gold:#efdf8e;
  --gold-line:#e6d57f;
  --paper:#ffffff;
  --hero-bg:#f7f7f7;
}
*{box-sizing:border-box;margin:0;padding:0}
html,body{width:1200px;height:3686px;overflow:hidden}
body{position:relative;background:var(--paper);font-family:"Montserrat",Arial,sans-serif;color:var(--ink)}
.abs{position:absolute}
.serif{font-family:"Playfair Display",Georgia,serif;font-weight:400}
.vline{position:absolute;width:2px;background:var(--gold-line)}

/* header */
.brand{left:0;width:1200px;top:50px;text-align:center;font-family:"Playfair Display",Georgia,serif;font-size:15px;letter-spacing:2px;color:var(--ink)}
.menu{left:1037px;top:47px;font-size:12px;display:flex;align-items:center;gap:10px}
.menu i{display:block;width:20px;height:2px;background:var(--ink);box-shadow:0 -6px 0 var(--ink),0 6px 0 var(--ink)}

/* hero */
.hero{left:0;top:0;width:1200px;height:692px;background:var(--hero-bg)}
.hero-photo{left:355px;top:104px;width:756px;height:495px;background:linear-gradient(135deg,#e9e9e9,#d8d8d8 55%,#cfc6a8)}
.hero-frame{left:988px;top:509px;width:143px;height:110px;border-right:2px solid var(--gold-line);border-bottom:2px solid var(--gold-line)}
.hero-title{left:92px;top:234px;font-size:35px;line-height:42px;letter-spacing:.5px}
.hero-sub{left:94px;top:334px;font-size:10px;line-height:16px;color:var(--text);width:240px}
.comp{left:92px;top:472px;width:411px;height:151px;background:var(--paper);box-shadow:0 6px 20px rgba(0,0,0,.06)}
.countdown{left:0;top:0;width:314px;height:71px;background:var(--navy);display:flex;align-items:center;justify-content:space-around;color:#ddd}
.countdown div{text-align:center;font-family:"Playfair Display",Georgia,serif;font-size:16px;line-height:16px;flex:1;border-right:1px solid #3b3b48}
.countdown div:last-child{border-right:none}
.countdown small{display:block;font-size:10px;letter-spacing:1px}
.tickets{left:314px;top:14px;width:97px;text-align:center;font-family:"Playfair Display",Georgia,serif;font-size:10px;line-height:12px;color:var(--text)}
.tickets b{display:block;font-weight:400;font-size:15px;color:var(--ink);line-height:18px}
.comp-name{left:23px;top:93px;width:205px;font-size:13px;line-height:18px}
.comp-enter{left:243px;top:103px;font-size:11px;letter-spacing:.3px;display:flex;align-items:center;gap:6px}

/* section headings */
.kicker{left:0;width:1200px;font-size:12px;letter-spacing:2px;color:var(--muted);text-align:center}
.heading{left:0;width:1200px;font-size:28px;text-align:center;letter-spacing:.5px}

/* packages */
.pack{top:920px;width:308px;height:210px;border:1px solid var(--line)}
.pack .price{position:absolute;left:50%;top:-34px;transform:translateX(-50%);background:var(--paper);padding:0 14px;font-size:52px;line-height:64px}
.pack p{position:absolute;left:0;right:0;top:54px;text-align:center;font-size:13px;line-height:21px;color:#333}
.btn-gold{position:absolute;left:89px;top:140px;width:130px;height:28px;background:var(--gold);font-size:11px;line-height:28px;text-align:center;color:#333}
.btn-gold::after{content:"";position:absolute;left:4px;top:4px;width:130px;height:28px;border-right:1px solid var(--line);border-bottom:1px solid var(--line)}

/* marble */
.marble{left:0;top:1220px;width:1200px;height:914px;background:linear-gradient(160deg,#f2f2f2,#e7e7e7 40%,#f0f0f0 70%,#e5e5e5)}
.card{background:var(--paper)}
.bracket-grey{border-left:2px solid #9a9a9a;border-bottom:2px solid #9a9a9a}
.who{left:103px;top:1302px;width:984px;height:276px}
.who-bracket{left:149px;top:1377px;width:66px;height:68px;border-left:2px solid var(--gold-line);border-top:2px solid var(--gold-line)}
.who-kicker{left:175px;top:1402px;font-size:13px;letter-spacing:1px;color:#444}
.who-title{left:175px;top:1418px;font-size:32px}
.who-photo{left:450px;top:1355px;width:251px;height:160px;border-radius:12px;background:linear-gradient(120deg,#d6d6d6,#8c8c8c 40%,#2a2a2a 55%,#9a9a9a 70%,#e4e4e4)}
.who-text{left:725px;top:1393px;width:320px;font-size:13px;line-height:23px;color:var(--text)}

.values{left:110px;top:1643px;width:981px;height:375px}
.values-bracket{left:520px;top:1679px;width:40px;height:40px;border-left:2px solid var(--gold-line);border-top:2px solid var(--gold-line)}
.values-title{left:537px;top:1690px;font-size:21px}
.value-line{left:277px;top:1807px;width:653px;height:1px;background:var(--gold-line)}
.value-icon{top:1760px;width:96px;height:96px;border-radius:50%;border:1.5px solid var(--gold-line);background:var(--paper);display:flex;align-items:center;justify-content:center}
.value-name{top:1876px;width:200px;text-align:center;font-size:14px;font-weight:500;letter-spacing:.5px}
.value-desc{top:1903px;width:170px;text-align:center;font-size:11px;line-height:17px;color:var(--muted)}

/* circles */
.ring{top:2211px;width:286px;height:286px;border-radius:50%;border:1px solid var(--line);background:var(--paper)}
.disc{position:absolute;left:7px;top:7px;width:270px;height:270px;border-radius:50%}
.disc-title{top:2312px;width:270px;text-align:center;font-size:21px;letter-spacing:1.5px}
.disc-text{top:2350px;width:200px;text-align:center;font-size:12px;line-height:20px;font-weight:500}

/* how to play */
.play{left:117px;top:2564px;width:984px;height:425px;box-shadow:0 10px 40px rgba(0,0,0,.07)}
.step-ring{top:2698px;width:138px;height:138px;border-radius:50%;border:2px solid var(--gold-line);display:flex;align-items:center;justify-content:center}
.step-num{top:2700px;z-index:2;font-family:"Playfair Display",Georgia,serif;font-size:100px;line-height:120px;color:transparent;-webkit-text-stroke:2px var(--gold-line)}
.step-label{top:2866px;width:200px;text-align:center;font-size:13px;font-weight:600}
.step-text{top:2888px;width:200px;text-align:center;font-size:13px;line-height:16px;color:var(--text)}

/* band */
.band{left:0;top:3047px;width:1200px;height:259px;background:linear-gradient(90deg,#4a4a4a,#2e2e2e 55%,#1c1c1c)}
.band-btn{left:472px;top:3146px;width:263px;height:60px;border:1px solid var(--gold-line);color:var(--gold);font-size:15px;letter-spacing:.5px;line-height:56px;text-align:center}
.band-btn::before{content:"";position:absolute;left:6px;top:6px;right:-8px;bottom:-8px;border:1px solid var(--gold-line)}

/* footer */
.fcol{top:3315px;height:303px;width:1px;background:#ddd}
.fhead{top:3368px;font-size:19px;letter-spacing:.5px;text-align:center}
.fbar{top:3406px;width:36px;height:2px;background:var(--gold-line)}
.flinks{top:3430px;text-align:center;font-size:11px;line-height:27px;color:#333}
.faddr{top:3430px;text-align:center;font-size:11px;line-height:16px;color:#333}
.input{left:828px;top:3435px;width:246px;height:37px;background:#f1f1f1;font-size:10px;line-height:37px;padding-left:18px;color:#555}
.subscribe{left:828px;top:3484px;width:246px;height:36px;background:var(--gold);font-size:11px;font-weight:600;text-align:center;line-height:36px}
.copy{left:0;width:1200px;top:3640px;text-align:center;font-size:11px;color:#333}
</style>
</head>
<body>

<!-- hero -->
<div class="abs hero"></div>
<div class="abs brand">THE KESTREL MARQUE</div>
<div class="abs menu">Menu <i></i></div>

<div class="abs hero-frame"></div>
<div class="abs hero-photo" role="img" aria-label="Three luxury dive watches, steel and gold, laid on white marble"></div>

<h1 class="abs serif hero-title">THE SIGNATURE<br>COLLECTION</h1>
<p class="abs hero-sub">To create a community where all members can feel a sense of belongings with another</p>

<div class="abs comp">
  <div class="abs countdown">
    <div>0<small>DAYS</small></div>
    <div>05<small>HOURS</small></div>
    <div>08<small>MIN</small></div>
    <div>28<small>SEC</small></div>
  </div>
  <div class="abs tickets">ONLY<b>44</b>TICKETS LEFT</div>
  <div class="abs serif comp-name">MARLOWE AZURE, NIGHTFALL &amp;<br>AMBER COMP</div>
  <div class="abs serif comp-enter">ENTER COMPETITION
    <svg width="16" height="10" viewBox="0 0 16 10"><path d="M0 5h14M10 1l4 4-4 4" fill="none" stroke="#1f1f1f" stroke-width="1.3"/></svg>
  </div>
</div>

<div class="vline" style="left:595px;top:666px;height:54px"></div>

<!-- packages -->
<div class="abs kicker" style="top:764px">OUR PACKAGES</div>
<h2 class="abs serif heading" style="top:780px">MEMBERSHIP PACKAGES</h2>

<div class="abs pack" style="left:114px">
  <span class="serif price">6.99</span>
  <p>BUYS YOU A<br>MEMBERSHIP + ONE ENTRY<br>TO THE MARLOWE .. DRAW</p>
  <span class="btn-gold">GET STARTED</span>
</div>
<div class="abs pack" style="left:438px">
  <span class="serif price">10.99</span>
  <p>BUYS YOU A<br>MEMBERSHIP + TWO ENTRY<br>TO THE MARLOWE .. DRAW</p>
  <span class="btn-gold">GET STARTED</span>
</div>
<div class="abs pack" style="left:760px">
  <span class="serif price">15</span>
  <p>BUYS YOU A<br>MEMBERSHIP + THREE ENTRY<br>TO THE MARLOWE .. DRAW</p>
  <span class="btn-gold">GET STARTED</span>
</div>

<div class="vline" style="left:598px;top:1192px;height:52px"></div>

<!-- marble section -->
<div class="abs marble" role="img" aria-label="Soft white marble texture background"></div>

<div class="abs bracket-grey" style="left:86px;top:1520px;width:89px;height:70px"></div>
<div class="abs card who"></div>
<div class="abs who-bracket"></div>
<div class="abs who-kicker">INTRODUCTION</div>
<h2 class="abs serif who-title">WHO WE ARE</h2>
<div class="abs who-photo" role="img" aria-label="Steel chronograph watch with black dial"></div>
<p class="abs who-text">A 100% Australian owned company whose main goal is to create a community for people who love what we love – luxury watches!</p>

<div class="vline" style="left:601px;top:1609px;height:51px"></div>

<div class="abs" style="left:972px;top:1929px;width:141px;height:108px;border-right:2px solid #9a9a9a;border-bottom:2px solid #9a9a9a"></div>
<div class="abs card values"></div>
<div class="abs values-bracket"></div>
<h2 class="abs serif values-title">OUR VALUES</h2>
<div class="abs value-line"></div>

<div class="abs value-icon" style="left:229px">
  <svg width="44" height="44" viewBox="0 0 44 44" fill="none" stroke="#444" stroke-width="1.5"><circle cx="22" cy="17" r="11"/><circle cx="22" cy="17" r="6"/><path d="M15 26l-4 12 5-3 3 5 3-10M29 26l4 12-5-3-3 5-3-10"/></svg>
</div>
<div class="abs value-icon" style="left:448px">
  <svg width="44" height="44" viewBox="0 0 44 44" fill="none" stroke="#444" stroke-width="1.5"><rect x="6" y="18" width="8" height="18"/><path d="M14 20l7-10c2-3 5-1 4 2l-2 6h11c3 0 3 4 0 4 3 0 3 4 0 4 3 0 3 4 0 4 2 0 2 4-1 4H14"/></svg>
</div>
<div class="abs value-icon" style="left:664px">
  <svg width="44" height="44" viewBox="0 0 44 44" fill="none" stroke="#444" stroke-width="1.5"><path d="M22 36L8 22c-5-5-1-14 6-14 4 0 6 2 8 5 2-3 4-5 8-5 7 0 11 9 6 14z"/><path d="M14 22l5-5 8 8M18 26l4 4M22 22l5 5"/></svg>
</div>
<div class="abs value-icon" style="left:882px">
  <svg width="44" height="44" viewBox="0 0 44 44" fill="none" stroke="#444" stroke-width="1.5"><circle cx="22" cy="22" r="16" stroke-dasharray="2 3"/><path d="M22 12v10l7 4"/></svg>
</div>

<div class="abs value-name" style="left:179px">LOYALTY</div>
<div class="abs value-desc" style="left:194px">We always have our customers and the community at the heart of what we do.</div>
<div class="abs value-name" style="left:397px">TRUST</div>
<div class="abs value-desc" style="left:412px">We're open and honest.</div>
<div class="abs value-name" style="left:615px">RESPECT</div>
<div class="abs value-desc" style="left:630px">We do what we say and say what we do.</div>
<div class="abs value-name" style="left:830px">COMMITMENT</div>
<div class="abs value-desc" style="left:845px">We ensure that we dedicate our time to deliver the best experience for you.</div>

<div class="vline" style="left:599px;top:2102px;height:79px"></div>

<!-- mission / vision / purpose -->
<div class="abs ring" style="left:150px">
  <div class="disc" role="img" aria-label="Close-up of a wristwatch on black" style="background:radial-gradient(circle at 60% 40%,#3a3a3a,#0d0d0d 70%)"></div>
</div>
<div class="abs ring" style="left:462px">
  <div class="disc" role="img" aria-label="Wristwatch on a wrist in dark grey tones" style="background:radial-gradient(circle at 45% 35%,#5a5a5a,#3c3c3c 70%)"></div>
</div>
<div class="abs ring" style="left:777px">
  <div class="disc" role="img" aria-label="Gold watch in warm yellow tones" style="background:radial-gradient(circle at 40% 60%,#f4e7a8,#e9d36a 70%)"></div>
</div>

<div class="abs serif disc-title" style="left:165px;color:#fff">OUR MISSION</div>
<div class="abs disc-text" style="left:193px;color:#fff">To create a community where all members can feel a sense of belongings with another. Our mission</div>
<div class="abs serif disc-title" style="left:470px;color:#fff">OUR VISION</div>
<div class="abs disc-text" style="left:505px;color:#fff">To help</div>
<div class="abs serif disc-title" style="left:787px;color:#333">OUR PURPOSE</div>
<div class="abs disc-text" style="left:820px;color:#333">Help us rebuild Australia one tree at a time.</div>

<div class="vline" style="left:602px;top:2535px;height:56px"></div>

<!-- how to play -->
<div class="abs card play"></div>
<div class="abs kicker" style="top:2613px">OUR PROCESS</div>
<h2 class="abs serif heading" style="top:2634px">HOW TO PLAY</h2>

<div class="abs step-ring" style="left:281px">
  <svg width="52" height="36" viewBox="0 0 52 36" fill="none" stroke="#444" stroke-width="1.5"><path d="M4 6h44v8a4 4 0 0 0 0 8v8H4v-8a4 4 0 0 0 0-8z"/><path d="M18 14h16M18 18h12M18 22h16"/></svg>
</div>
<div class="abs step-num" style="left:262px">1</div>
<div class="abs step-ring" style="left:543px">
  <svg width="40" height="44" viewBox="0 0 40 44" fill="none" stroke="#444" stroke-width="1.5"><rect x="6" y="4" width="28" height="36"/><path d="M12 14h16M12 20h16M12 26h16M12 32h10"/></svg>
</div>
<div class="abs step-num" style="left:515px">2</div>
<div class="abs step-ring" style="left:802px">
  <svg width="46" height="46" viewBox="0 0 46 46" fill="none" stroke="#444" stroke-width="1.5"><circle cx="23" cy="25" r="14"/><path d="M23 16l3 6 6 1-4.5 4 1 6-5.5-3-5.5 3 1-6-4.5-4 6-1z"/><path d="M23 4v5M11 8l3 4M35 8l-3 4"/></svg>
</div>
<div class="abs step-num" style="left:777px">3</div>

<svg class="abs" style="left:432px;top:2752px" width="85" height="30" viewBox="0 0 85 30" fill="none" stroke="#c8c8c8" stroke-width="1.5"><path d="M2 22c25-14 50-14 78-6M72 10l8 6-9 3"/></svg>
<svg class="abs" style="left:695px;top:2745px" width="85" height="30" viewBox="0 0 85 30" fill="none" stroke="#c8c8c8" stroke-width="1.5"><path d="M2 18c25-12 50-12 78 0M72 11l8 7-9 2"/></svg>

<div class="abs step-label" style="left:245px">STEP 1</div>
<div class="abs step-text" style="left:245px">Pick a package.</div>
<div class="abs step-label" style="left:510px">STEP 2</div>
<div class="abs step-text" style="left:510px">Enter Details</div>
<div class="abs step-label" style="left:759px">STEP 3</div>
<div class="abs step-text" style="left:759px">Wait for draw –<br>its that simple!</div>

<!-- call to action band -->
<div class="abs band" role="img" aria-label="Black and white photo of a chronograph watch on a wrist"></div>
<div class="vline" style="left:613px;top:2984px;height:98px"></div>
<div class="abs band-btn">GET START COMPETITION</div>

<!-- footer -->
<div class="abs fcol" style="left:420px"></div>
<div class="abs fcol" style="left:755px"></div>

<div class="abs serif fhead" style="left:130px;width:280px">QUICK LINKS</div>
<div class="abs fbar" style="left:252px"></div>
<div class="abs flinks" style="left:130px;width:280px">ABOUT US<br>FAQS<br>CONTACT US<br>TERMS &amp; CONDITIONS</div>

<div class="abs serif fhead" style="left:455px;width:280px">CONTACT US</div>
<div class="abs fbar" style="left:577px"></div>
<div class="abs faddr" style="left:455px;width:280px">ADDRESS<br>14 HARROW LANE BRIGHTVALE<br>VIC 3190.<br><br>INFO@THEKESTRELMARQUE.COM.AU<br><br>0400 555 019.</div>

<div class="abs serif fhead" style="left:795px;width:280px">SUBSCRIBE EMAIL</div>
<div class="abs fbar" style="left:917px"></div>
<div class="abs input">YOUR EMAIL</div>
<div class="abs subscribe">SUBSCRIBE NOW</div>

<div class="abs copy">COPYRIGHT © 2021 THE KESTREL MARQUE</div>

</body>
</html>
```